VFX Company Business Card Design Project

The Ember Vale is a decentralized Visual Effects Studio servicing the television and feature film industries.
Project Brief:
Take our logo that was previously designed on Pixel Harbor and make a double sided business card.
Requirements:
- Card MUST be double sided.
- Front of card MUST have the yellow part of our logo against the dark grey background.
- Back of card is completely up to the designer.
- Back of card must include the complete company logo.
Please follow these File Preparation guidelines:
http://printmoor.example/infopage?file=filetype_en&s=PrintMoor_new&lang=en
Industry/Entity Type
Business
Look and feel
Each slider illustrates characteristics of the customer's brand and the style your logo design should communicate.

```html
<!DOCTYPE html>
<html lang="en">
<head>
<meta charset="utf-8">
<title>The Ember Vale – Business Cards</title>
<link rel="stylesheet" href="https://fonts.googleapis.com/css2?family=Josefin+Sans:wght@400;600&family=Montserrat:wght@700&family=Open+Sans:wght@400;700&display=swap">
<style>
  :root {
    --stage: #7a4524;
    --card: #2a2a2a;
    --yellow: #fec42e;
    --slate: #5d676b;
    --ivory: #eef0e6;
    --white: #f4f4f0;
    --ink: #222222;
  }
  * { box-sizing: border-box; margin: 0; padding: 0; }
  html, body { width: 1200px; height: 733px; overflow: hidden; }
  body { background: var(--stage); position: relative; font-family: "Open Sans", sans-serif; }

  .card {
    position: absolute;
    background: var(--card);
    border-radius: 26px;
    overflow: hidden;
  }
  .card--front    { left: 70px;  top: 43px;  width: 522px; height: 300px; }
  .card--contact  { left: 630px; top: 48px;  width: 524px; height: 298px; }
  .card--lockup   { left: 66px;  top: 384px; width: 524px; height: 300px; }
  .card--wordmark { left: 625px; top: 388px; width: 523px; height: 298px; }

  .brand-name {
    font-family: "Montserrat", sans-serif;
    font-weight: 700;
    text-transform: uppercase;
    white-space: nowrap;
    letter-spacing: 0.02em;
  }
  .brand-mark {
    display: inline-block;
    border-radius: 50%;
    flex: none;
  }

  /* Front */
  .card--front .brand {
    position: absolute; inset: 0;
    display: flex; align-items: center; justify-content: center; gap: 22px;
  }
  .card--front .brand-mark { width: 70px; height: 70px; border: 14px solid var(--yellow); }
  .card--front .brand-name { color: var(--yellow); font-size: 40px; }

  /* Contact side */
  .card--contact .brand-name {
    position: absolute; top: 40px; left: 0; right: 0; text-align: center;
    color: var(--slate); font-size: 54px; letter-spacing: 0;
  }
  .address {
    position: absolute; top: 164px; left: 0; right: 0; text-align: center;
    color: var(--white); font-family: "Josefin Sans", sans-serif; font-size: 15px; letter-spacing: 0.06em;
  }
  .card--contact .wave { position: absolute; left: 0; top: 0; width: 524px; height: 298px; }
  .person { position: absolute; left: 45px; top: 252px; color: var(--ink); }
  .person-name { font-weight: 700; font-size: 18px; line-height: 1.1; }
  .person-title { font-size: 14px; margin-top: 4px; }
  .contact-list {
    position: absolute; right: 27px; top: 224px; list-style: none;
    font-size: 13px; line-height: 17px; color: var(--ink); text-align: right;
  }
  .contact-list li { display: flex; align-items: center; justify-content: flex-end; gap: 4px; }
  .contact-list svg { width: 10px; height: 10px; }

  /* Lockup side */
  .card--lockup .brand {
    position: absolute; left: 0; right: 0; top: 112px;
    display: flex; align-items: center; justify-content: center; gap: 16px;
  }
  .card--lockup .brand-mark { width: 46px; height: 46px; border: 9px solid var(--yellow); }
  .card--lockup .brand-name { color: var(--slate); font-size: 36px; }

  .card--wordmark .brand-name {
    position: absolute; top: 100px; left: 0; right: 0; text-align: center;
    color: var(--slate); font-size: 52px; letter-spacing: 0;
  }

  .web {
    position: absolute; left: 0; right: 0; bottom: 26px; text-align: center;
    color: var(--white); font-family: "Josefin Sans", sans-serif; font-size: 18px; letter-spacing: 0.14em;
  }
</style>
</head>
<body>

<section class="card card--front" aria-label="Card front">
  <div class="brand">
    <span class="brand-mark"></span>
    <span class="brand-name">The Ember Vale</span>
  </div>
</section>

<section class="card card--contact" aria-label="Card back with contact details">
  <svg class="wave" viewBox="0 0 524 298" aria-hidden="true">
    <path d="M0,172 Q170,250 524,190 L524,298 L0,298 Z" fill="var(--yellow)"/>
    <path d="M0,186 Q200,262 524,202 L524,298 L0,298 Z" fill="var(--slate)"/>
    <path d="M0,194 Q200,268 524,210 L524,298 L0,298 Z" fill="var(--ivory)"/>
  </svg>
  <div class="brand-name">The Ember Vale</div>
  <p class="address">00, Complex name, City, State 0042</p>
  <div class="person">
    <p class="person-name">Your Name</p>
    <p class="person-title">Title</p>
  </div>
  <ul class="contact-list">
    <li><svg viewBox="0 0 10 10"><path d="M2,0 L4,2 L3,4 Q4,6 6,7 L8,6 L10,8 L8,10 Q1,9 0,2 Z" fill="var(--ink)"/></svg>0987 654321</li>
    <li><svg viewBox="0 0 10 10"><rect x="0" y="3" width="10" height="6" rx="1" fill="var(--ink)"/><rect x="2" y="0" width="6" height="3" fill="var(--ink)"/></svg>0987 654321</li>
    <li><svg viewBox="0 0 10 10"><rect x="0" y="2" width="10" height="7" fill="var(--ink)"/><path d="M0,2 L5,6 L10,2" stroke="var(--ivory)" fill="none"/></svg>info@embervale.example</li>
    <li><svg viewBox="0 0 10 10"><circle cx="5" cy="5" r="4.5" fill="var(--ink)"/><path d="M0.5,5 H9.5 M5,0.5 V9.5" stroke="var(--ivory)" stroke-width="0.8"/></svg>www.embervale.example</li>
  </ul>
</section>

<section class="card card--lockup" aria-label="Card back with full logo">
  <div class="brand">
    <span class="brand-mark"></span>
    <span class="brand-name">The Ember Vale</span>
  </div>
  <p class="web">www.embervale.example</p>
</section>

<section class="card card--wordmark" aria-label="Card back with wordmark">
  <div class="brand-name">The Ember Vale</div>
  <p class="web">www.embervale.example</p>
</section>

</body>
</html>
```